Custom Home Builder Needs a Website

Harbor Pine Builders Ltd. requires a clean professional 5 page website - Home, About Us, Gallery (Interior and Exterior), Our Process and Contact Us(with registration form). We are a home builder who also has homes for sale. Also please have a place for video embedding. Editable fields by user. Using the stationery 'feel' that is attached. Need social media links. If you require any additional files, please request.

Target Market(s)

Families and professionals

Industry/Entity Type

Home Builder

Coding

Coded - Design and coding required

Number of Pages Required

5+ page

Font styles to use
Sans Serif
Other font styles liked:
• Lato

Requirements
Must have
• Editable by user
• Register Button
• Place to put home models for sale - preferably on the first page
• 5 page website -
• -Home
• -About Us
• -Gallery (Interior and Exterior)
• -Our Process
• -Contact Us.
Nice to have
• Themed similar to current stationery
• place for video embedding
• Try some darker backgrounds
• Change pictures to B/W if works for design
Should not have
• cartoonish type of content

```html
<!DOCTYPE html>
<html lang="en">
<head>
<meta charset="utf-8">
<title>Harbor Pine Builders Ltd.</title>
<link href="https://fonts.googleapis.com/css2?family=Lato:wght@300;400;700;900&family=Great+Vibes&display=swap" rel="stylesheet">
<style>
:root{
  --green:#3ccf00;
  --green-dark:#2aa100;
  --ink:#1c1c1c;
  --text:#555;
  --muted:#777;
  --light:#f3f3f3;
  --footer:#3a3a3a;
  --footer-text:#d6d6d6;
  --white:#fff;
}
*{box-sizing:border-box;margin:0;padding:0}
html,body{width:1200px;height:3448px;overflow:hidden}
body{position:relative;font-family:'Lato',sans-serif;color:var(--text);background:var(--white)}
.abs{position:absolute}
/* hero */
.hero{left:0;top:0;width:1200px;height:770px;background:linear-gradient(180deg,#b9cbd9 0%,#8a8a7c 35%,#4d4a45 60%,#5f7a3a 85%,#7d9a4a 100%)}
.hero-arch{left:0;top:540px;width:1200px;height:240px}
.site-brand{left:90px;top:22px;color:var(--white);font-weight:700;font-size:17px;letter-spacing:1px;display:flex;align-items:center;gap:10px}
.site-brand .mark{width:18px;height:18px;background:var(--green)}
.nav{right:80px;top:38px;display:flex;gap:42px;font-size:15px;color:var(--ink);text-transform:uppercase}
.nav .active{color:var(--green)}
.hero-brand{left:0;width:1200px;top:200px;text-align:center;color:var(--white);font-weight:700;font-size:30px;letter-spacing:3px}
.hero-brand small{display:block;font-size:12px;letter-spacing:12px;font-weight:400;margin-top:8px}
.hero-tag{left:0;width:1200px;top:300px;text-align:center;font-family:'Great Vibes',cursive;font-size:66px;color:var(--green)}
.btn-hero{left:486px;top:440px;width:228px;height:50px;border-radius:25px;background:rgba(200,200,200,.85);color:var(--white);font-size:13px;text-transform:uppercase;display:flex;align-items:center;padding-left:28px}
.btn-hero span{position:absolute;right:0;top:0;width:50px;height:50px;border-left:1px solid rgba(255,255,255,.6);display:flex;align-items:center;justify-content:center}
/* headings */
.sec-title{left:0;width:1200px;text-align:center;font-weight:700;font-size:42px;color:var(--ink);letter-spacing:1px}
.divider{left:480px;width:240px;height:20px}
/* about */
.about-text{left:260px;width:680px;top:738px;text-align:center;font-size:15.5px;line-height:26px;color:var(--muted)}
.step{width:130px;text-align:center;font-size:19px;color:var(--ink);text-transform:uppercase}
.step .ring{width:126px;height:126px;border-radius:50%;background:var(--light);margin:0 auto 16px;display:flex;align-items:center;justify-content:center}
.step .ring.on{background:var(--white);border:3px solid var(--green-dark)}
.grey-band{left:0;top:1160px;width:1200px;height:700px;background:var(--light)}
.video{left:396px;top:1100px;width:410px;height:252px;background:linear-gradient(180deg,#8d8f92,#5f6a5a);border:6px solid var(--white);box-shadow:0 3px 8px rgba(0,0,0,.3)}
.play{left:169px;top:94px;width:52px;height:52px;border-radius:50%;background:var(--white);display:flex;align-items:center;justify-content:center}
/* projects */
.card{top:1510px;width:334px}
.card .ph{height:208px;position:relative}
.card h3{font-weight:400;font-size:18px;color:var(--ink);text-align:center;margin-top:18px}
.card p{font-size:13.5px;line-height:21px;color:var(--muted);text-align:center;margin-top:6px;padding:0 20px}
.badge{position:absolute;left:0;top:0;background:var(--green);color:var(--white);font-size:12px;padding:6px 16px}
.btn-green{background:var(--green);color:var(--white);font-size:13px;font-weight:700;text-transform:uppercase;border-radius:26px;display:flex;align-items:center;justify-content:center}
/* testimonials */
.testi{left:0;top:1862px;width:1200px;height:460px;background:linear-gradient(180deg,#eeeeec,#e2e2de)}
.avatar{left:554px;top:2026px;width:92px;height:92px;border-radius:50%;background:linear-gradient(180deg,#b9a089,#6d6f7a);border:5px solid #ccc}
.arrow-box{top:2051px;width:40px;height:30px;display:flex;align-items:center;justify-content:center}
.quote{left:190px;width:820px;top:2142px;text-align:center;font-size:16px;line-height:26px;color:#444}
.author{left:0;width:1200px;top:2240px;text-align:center;font-size:21px;color:#333}
.qmark{font-family:Georgia,serif;font-size:90px;color:var(--green);line-height:1}
/* gallery */
.g{width:334px;height:250px}
/* footer */
.footer{left:0;top:3115px;width:1200px;height:333px;background:var(--footer);color:var(--footer-text)}
.f-col h4{font-weight:400;font-size:20px;color:var(--white);margin-bottom:18px}
.f-col{font-size:14px;line-height:22px}
.news-in{display:flex;width:332px;height:38px;background:#888;margin-top:22px;font-size:12px;color:#ddd;align-items:center;padding-left:14px}
.news-in b{margin-left:auto;border-left:1px solid #bbb;padding:0 14px;font-weight:700;color:var(--white)}
.social{display:flex;gap:16px;align-items:center;font-size:20px;color:var(--white)}
.social i{display:block;width:14px;height:14px;border-radius:50%;background:var(--green)}
.ql li{list-style:none;display:flex;align-items:center;gap:10px;margin-bottom:6px}
.ql li::before{content:"";width:5px;height:5px;background:var(--green);border-radius:50%}
.ql li.on{color:var(--green)}
.news-item{display:flex;gap:14px;margin-bottom:16px}
.news-item .pic{width:54px;height:54px;border-radius:50%;background:linear-gradient(#c9b8a6,#6b6f78);flex:none}
.news-item em{display:block;color:var(--green);font-size:12px}
.copy{right:90px;top:3404px;color:var(--white);font-size:13px;font-weight:700}
.copy span{color:var(--ink)}
</style>
</head>
<body>

<div class="abs hero" role="img" aria-label="Photograph of a stone-fronted two-storey home with grey garage doors and a green lawn under a hillside sky"></div>
<svg class="abs hero-arch" viewBox="0 0 1200 240" preserveAspectRatio="none">
  <path d="M0 230 Q600 -30 1200 230 L1200 240 L0 240Z" fill="#fff"/>
  <path d="M0 230 Q600 -30 1200 230" fill="none" stroke="#3ccf00" stroke-width="9"/>
</svg>

<div class="abs site-brand"><span class="mark"></span>Harbor Pine Builders Ltd.</div>
<nav class="abs nav"><span class="active">Home</span><span>About Us</span><span>Gallery</span><span>Our Process</span><span>Contact</span></nav>

<div class="abs hero-brand">HARBOR PINE BUILDERS LTD.<small>DESIGN · BUILD</small></div>
<div class="abs hero-tag">Largest Pine Homes Builders</div>
<div class="abs btn-hero">Contact Us Now<span><svg width="16" height="12" viewBox="0 0 16 12"><path d="M2 1l5 5-5 5M9 1l5 5-5 5" fill="none" stroke="#fff" stroke-width="1.6"/></svg></span></div>

<h2 class="abs sec-title" style="top:628px">ABOUT US</h2>
<svg class="abs divider" style="top:690px" viewBox="0 0 240 20"><line x1="0" y1="10" x2="240" y2="10" stroke="#333"/><path d="M110 10l10-7 10 7-10 7z" fill="#555"/></svg>
<p class="abs about-text">Lorem Ipsum is simply dummy text of the printing and typesetting industry. Lorem Ipsum has been the industry's standard dummy text ever since the 1500s, when an unknown printer took a galley of type and scrambled it to make a type specimen book.</p>

<svg class="abs" style="left:360px;top:870px" width="480" height="60" viewBox="0 0 480 60"><path d="M10 50 Q110 0 200 40M280 40 Q370 0 470 50" fill="none" stroke="#ccc" stroke-dasharray="4 5"/></svg>
<div class="abs step" style="left:210px;top:852px"><div class="ring"><svg width="60" height="60" viewBox="0 0 60 60" fill="none" stroke="#222" stroke-width="2.5"><rect x="12" y="14" width="36" height="30" transform="rotate(-12 30 30)"/><path d="M14 48 L46 48 L14 22Z"/></svg></div>Design</div>
<div class="abs step" style="left:535px;top:875px"><div class="ring on"><svg width="60" height="60" viewBox="0 0 60 60" fill="none" stroke="#222" stroke-width="2.5"><path d="M30 10 L52 22 L30 34 L8 22Z M8 22 V42 L30 54 L52 42 V22 M30 34 V54"/></svg></div>Build</div>
<div class="abs step" style="left:860px;top:852px"><div class="ring"><svg width="60" height="60" viewBox="0 0 60 60" fill="none" stroke="#222" stroke-width="2.5"><path d="M8 30 L30 10 L52 30 M14 26 V50 H46 V26"/><rect x="22" y="34" width="8" height="8"/><rect x="33" y="34" width="8" height="8"/></svg></div>Live</div>

<div class="abs grey-band"></div>
<svg class="abs" style="left:0;top:1170px" width="1200" height="130" viewBox="0 0 1200 130"><path d="M40 20 Q250 120 420 125 L420 130 Q230 125 40 20Z" fill="#3ccf00"/><path d="M1160 20 Q950 120 780 125 L780 130 Q970 125 1160 20Z" fill="#3ccf00"/></svg>
<div class="abs video" role="img" aria-label="Video thumbnail of a finished two-storey home"><div class="abs play"><svg width="16" height="18" viewBox="0 0 16 18"><path d="M2 1 L15 9 L2 17Z" fill="#333"/></svg></div></div>

<h2 class="abs sec-title" style="top:1400px">PROJECTS</h2>
<svg class="abs divider" style="top:1462px" viewBox="0 0 240 20"><line x1="0" y1="10" x2="240" y2="10" stroke="#333"/><path d="M110 10l10-7 10 7-10 7z" fill="#555"/></svg>

<div class="abs card" style="left:78px"><div class="ph" role="img" aria-label="Photograph of a dark-sided craftsman home with a double garage" style="background:linear-gradient(180deg,#cfd8e0,#545a5e 55%,#4f7a36)"></div><h3>Project Name</h3><p>Lorem Ipsum is simply dummy text of the printing and typesetting industry.</p></div>
<div class="abs card" style="left:434px"><div class="ph" role="img" aria-label="Photograph of a home for sale with stone trim" style="background:linear-gradient(180deg,#6d7175,#3f4447 55%,#3d5433)"><span class="badge">on sale</span><div class="abs btn-green" style="left:94px;top:80px;width:148px;height:46px">View Detail</div></div><h3>Project Name</h3><p>Lorem Ipsum is simply dummy text of the printing and typesetting industry.</p></div>
<div class="abs card" style="left:789px"><div class="ph" role="img" aria-label="Photograph of a grey two-storey home with a white garage door" style="background:linear-gradient(180deg,#d9e1e8,#6a6e70 55%,#5b8a3c)"></div><h3>Project Name</h3><p>Lorem Ipsum is simply dummy text of the printing and typesetting industry.</p></div>

<div class="abs testi" role="img" aria-label="Soft background photograph of a bright home office"></div>
<h2 class="abs sec-title" style="top:1910px">TESTIMONIALS</h2>
<svg class="abs divider" style="top:1970px" viewBox="0 0 240 20"><line x1="0" y1="10" x2="240" y2="10" stroke="#333"/><path d="M110 10l10-7 10 7-10 7z" fill="#555"/></svg>
<div class="abs arrow-box" style="left:458px;background:#e4e4e4;border:1px solid #999"><svg width="16" height="10" viewBox="0 0 16 10"><path d="M15 5H2M6 1L2 5l4 4" fill="none" stroke="#444" stroke-width="1.8"/></svg></div>
<div class="abs avatar" role="img" aria-label="Client portrait"></div>
<div class="abs arrow-box" style="left:700px;background:#4a4a4a"><svg width="16" height="10" viewBox="0 0 16 10"><path d="M1 5h13M10 1l4 4-4 4" fill="none" stroke="#fff" stroke-width="1.8"/></svg></div>
<div class="abs qmark" style="left:128px;top:2112px">&ldquo;</div>
<p class="abs quote">Northgate Law has met and exceeded our expectations in assisting our company with our real estate legal needs. In an area of law where the rules our ever changing, we simply could not navigate our company effectively without their help.</p>
<div class="abs qmark" style="left:1024px;top:2190px">&rdquo;</div>
<div class="abs author">- Calder Commercial</div>

<h2 class="abs sec-title" style="top:2370px">GALLERY</h2>
<svg class="abs divider" style="top:2432px" viewBox="0 0 240 20"><line x1="0" y1="10" x2="240" y2="10" stroke="#333"/><path d="M110 10l10-7 10 7-10 7z" fill="#555"/></svg>
<div class="abs g" style="left:78px;top:2469px;background:linear-gradient(180deg,#dfe6ec,#5b5e60 55%,#5e8a3e)" role="img" aria-label="Exterior photograph of a home with stone columns"></div>
<div class="abs g" style="left:434px;top:2469px;background:linear-gradient(180deg,#5a3d2a,#3b2a20 60%,#7d6a55)" role="img" aria-label="Interior photograph of a kitchen with dark wood cabinets"></div>
<div class="abs g" style="left:789px;top:2469px;background:linear-gradient(180deg,#e3e8ec,#5d6265 55%,#8a8a86)" role="img" aria-label="Exterior photograph of a grey home with white trim"></div>
<div class="abs g" style="left:78px;top:2740px;background:linear-gradient(180deg,#bcc8cc,#a9b3b0 55%,#c9a6b4)" role="img" aria-label="Interior photograph of a child's bedroom"></div>
<div class="abs g" style="left:434px;top:2740px;background:linear-gradient(180deg,#cdd6df,#5d666c 55%,#7a6a55)" role="img" aria-label="Exterior photograph of a blue-grey home with a triple garage"></div>
<div class="abs g" style="left:789px;top:2740px;background:linear-gradient(180deg,#e9e7e2,#c5c1b8 55%,#9a9690)" role="img" aria-label="Interior photograph of a bright bathroom with glass shower"></div>
<div class="abs btn-green" style="left:528px;top:3010px;width:144px;height:50px">View All</div>

<footer class="abs footer">
  <div class="abs f-col" style="left:80px;top:34px;width:340px"><h4>Newsletter</h4>Sign Up to Our Newsletter to Get Latest<br>News &amp; Updates
    <div class="news-in">Enter E-mail Id<b>SUBSCRIBE</b></div>
    <div class="social" style="margin-top:26px">Follow Us On : <i></i><i></i><i></i><i></i><i></i></div>
  </div>
  <div class="abs f-col" style="left:460px;top:34px;width:220px"><h4>Contact Us</h4>
    <div style="display:flex;gap:12px"><svg width="14" height="20" viewBox="0 0 14 20"><path d="M7 0a7 7 0 0 1 7 7c0 5-7 13-7 13S0 12 0 7a7 7 0 0 1 7-7z" fill="#3ccf00"/><circle cx="7" cy="7" r="2.5" fill="#3a3a3a"/></svg><span>PO Box 218<br>Lakeview, SK, S0K 2B0<br><u>VIEW ON MAP</u></span></div>
    <div style="display:flex;gap:12px;margin-top:10px"><svg width="16" height="16" viewBox="0 0 16 16"><path d="M3 1l3 3-2 2c1 2 3 4 5 5l2-2 3 3-2 3C7 15 1 9 1 3z" fill="#3ccf00"/></svg>306-555-0142</div>
    <div style="display:flex;gap:12px;margin-top:10px"><svg width="16" height="12" viewBox="0 0 16 12"><rect width="16" height="12" fill="#3ccf00"/><path d="M0 0l8 6 8-6" fill="none" stroke="#3a3a3a" stroke-width="1.5"/></svg>info@harborpinebuilders.ca</div>
  </div>
  <div class="abs f-col" style="left:708px;top:34px;width:240px"><h4>Latest News</h4>
    <div class="news-item"><div class="pic" role="img" aria-label="News author portrait"></div><div>Lorem Ipsum is simply dummy text of the.<em>12th June, 2016</em></div></div>
    <div class="news-item"><div class="pic" role="img" aria-label="News author portrait"></div><div>Lorem Ipsum is simply dummy text of the.<em>12th June, 2016</em></div></div>
  </div>
  <div class="abs f-col" style="left:968px;top:34px;width:160px"><h4>Quick Links</h4>
    <ul class="ql"><li class="on">Home</li><li>About</li><li>Gallery</li><li>Our Process</li><li>Contact</li></ul>
  </div>
</footer>
<svg class="abs" style="left:0;top:3360px" width="1200" height="88" viewBox="0 0 1200 88"><path d="M0 88 V60 Q300 20 700 40 Q1000 55 1200 10 V88Z" fill="#3ccf00"/><path d="M0 60 Q300 20 700 40 Q1000 55 1200 10" fill="none" stroke="#fff" stroke-width="6"/></svg>
<div class="abs copy">© HARBOR PINE BUILDERS LTD. <span>- 2016. All Rights Reserved.</span></div>

</body>
</html>
```